Geschäftspapiere für Handwerksunternehmen
Zielgruppe
Handwerk
Elektroinstallation
Design Modern
Aufgabenstellung
Anschrift, Kontaktdaten, Bankverbindung, Logo,
Im Lindengrund 7 47391 Wendelstedt Inhaber Jonas Velbrück
Telefon: 04128-6350712 Email: info@trolvane-elektrotechnik.de Internet: www.trolvane-elektrotechnik.de
Finanzamt Hobrachtal USt.-ID: DE574036218 Steuer Nr.:3196450721
Kreiskasse Wendorn IBAN:DE71430982160004197356 BIC:WKRNDEF1WDN

```html
<!DOCTYPE html>
<html lang="de">
<head>
<meta charset="utf-8">
<title>Trolvane Elektrotechnik – Geschäftspapiere</title>
<link href="https://fonts.googleapis.com/css2?family=PT+Sans:wght@400;700&display=swap" rel="stylesheet">
<style>
:root{
  --bg:#b3b3b3;
  --paper:#ffffff;
  --ink:#151515;
  --yellow:#f1e41c;
  --slate:#6f7785;
  --text-grey:#8a8a8a;
  --glow:#f0a43a;
}
*{margin:0;padding:0;box-sizing:border-box}
html,body{width:1200px;height:840px;overflow:hidden}
body{background:var(--bg);font-family:"PT Sans",sans-serif;position:relative}
.sheet,.envelope{position:absolute;background:var(--paper);overflow:hidden}

/* letterhead */
.letterhead{left:39px;top:55px;width:504px;height:713px}
.letterhead__header{position:absolute;left:0;top:0;width:504px;height:99px;background:var(--ink)}
.photo-bulbs{position:absolute;left:0;top:0;height:100%;
  background:radial-gradient(ellipse at 38% 45%,#ffd98a 0%,var(--glow) 14%,#6b3a12 36%,#1e1a17 65%,var(--ink) 100%)}
.letterhead .photo-bulbs{width:150px}
.brand{position:absolute;color:var(--yellow);font-weight:700;line-height:1}
.brand__name{display:block;letter-spacing:2px}
.brand__sub{display:block}
.letterhead .brand{left:176px;top:26px}
.letterhead .brand__name{font-size:31px}
.letterhead .brand__sub{font-size:11.5px;margin-top:4px;text-align:right}
.contact-list{position:absolute;left:362px;top:18px;list-style:none;color:#e8e8e8;font-size:7px;font-weight:700}
.contact-list li{display:flex;align-items:center;height:21px;white-space:nowrap}
.contact-list svg{width:11px;height:11px;margin-right:5px;flex:none}
.return-address{position:absolute;left:97px;top:119px;font-size:6.5px;color:var(--text-grey);
  border-bottom:1px solid var(--text-grey);padding-bottom:2px;white-space:nowrap}
.fold-mark{position:absolute;left:7px;width:0;height:0;border-top:3px solid transparent;border-bottom:3px solid transparent;border-left:9px solid var(--yellow)}
.footer-rule{position:absolute;left:0;top:656px;width:504px;height:1px;background:#5a4a45}
.service-icons{position:absolute}
.service-icons svg{position:absolute;width:26px;height:28px;fill:var(--slate);stroke:var(--slate)}
.service-band{position:absolute;left:0}
.service-band text{font-family:"PT Sans",sans-serif;font-size:6.2px;fill:var(--yellow)}
.bank-details{position:absolute;top:666px;font-family:Arial,sans-serif;font-size:5.4px;line-height:7.6px;color:var(--slate);white-space:nowrap}
.web{position:absolute;display:flex;align-items:center;color:var(--slate);font-size:9.5px;white-space:nowrap}
.web svg{width:12px;height:12px;margin-right:6px;stroke:var(--slate);fill:none}

/* envelopes */
.envelope--flap{left:595px;top:107px;width:557px;height:279px}
.envelope__flap{position:absolute;left:0;top:0}
.envelope--flap .brand{left:0;width:557px;top:26px;text-align:center}
.envelope--flap .brand__name{font-size:26px}
.envelope--flap .brand__sub{font-size:9px;margin-top:3px}

.envelope--window{left:595px;top:420px;width:557px;height:279px}
.sender-banner{position:absolute;left:28px;top:23px;width:205px;height:73px;background:var(--ink)}
.sender-banner .photo-bulbs{width:100px}
.sender-banner .brand{right:10px;top:24px;text-align:right}
.sender-banner .brand__name{font-size:18px;letter-spacing:1px}
.sender-banner .brand__sub{font-size:6.5px;margin-top:2px}
.sender-address{position:absolute;left:389px;top:234px;display:flex;align-items:center;color:var(--slate);font-size:9px;font-weight:700;white-space:nowrap}
.sender-address svg{width:13px;height:13px;margin-right:5px}
</style>
</head>
<body>

<svg width="0" height="0" style="position:absolute" aria-hidden="true">
  <symbol id="icon-bulb" viewBox="0 0 26 28">
    <g fill="none" stroke-width="1.2">
      <path d="M13 7a6 6 0 0 0-4 10.5c1 1 1.5 2 1.5 3.5h5c0-1.5.5-2.5 1.5-3.5A6 6 0 0 0 13 7z"/>
      <path d="M10.5 23h5M11 25h4M13 21v-6l-2-2M13 15l2-2"/>
      <path d="M13 1v3M5 4l2 2M21 4l-2 2M2 10h3M24 10h-3M8 2l1 2.5M18 2l-1 2.5"/>
    </g>
  </symbol>
  <symbol id="icon-bolt" viewBox="0 0 26 28"><path stroke="none" d="M15 1L8 15h5l-3 12 8-16h-5l3-10z"/></symbol>
  <symbol id="icon-house" viewBox="0 0 26 28"><path stroke="none" d="M13 4L0 17h3v10h20V17h3zM11 19h4v4h-4z"/><rect x="11" y="19" width="4" height="4" fill="#fff" stroke="none"/></symbol>
  <symbol id="icon-solar" viewBox="0 0 26 28"><circle cx="21" cy="6" r="3" stroke="none"/><path stroke-width="0.8" d="M21 1v1.5M25.5 6H24M24 2.5l-1 1M17.5 2.5l1 1"/><path stroke="none" d="M4 10h16l3 11H1z"/><path stroke="#fff" stroke-width="0.6" d="M3 13.5h18M2 17h20M8 10l-2 11M12 10v11M16 10l2 11"/><path stroke-width="1.2" d="M12 21v5M8 26h8"/></symbol>
  <symbol id="icon-pin" viewBox="0 0 12 12"><circle cx="6" cy="6" r="5.5" fill="var(--yellow)"/><path d="M3 6l6-3-3 6-.5-2.5z" fill="var(--ink)"/></symbol>
  <symbol id="icon-phone" viewBox="0 0 12 12"><circle cx="6" cy="6" r="5.5" fill="var(--yellow)"/><path d="M4 3.2l1 1.3-.6.8c.5 1 1.3 1.8 2.3 2.3l.8-.6 1.3 1-.7 1C5.8 8.8 3.2 6.2 3 4z" fill="var(--ink)"/></symbol>
  <symbol id="icon-mail" viewBox="0 0 12 12"><circle cx="6" cy="6" r="5.5" fill="var(--yellow)"/><text x="6" y="8.3" text-anchor="middle" font-size="7" font-weight="700" font-family="Arial,sans-serif" fill="var(--ink)">@</text></symbol>
  <symbol id="icon-globe" viewBox="0 0 12 12"><circle cx="6" cy="6" r="5.3"/><ellipse cx="6" cy="6" rx="2.3" ry="5.3"/><path d="M.7 6h10.6M1.6 3.3h8.8M1.6 8.7h8.8"/></symbol>
</svg>

<!-- Briefbogen -->
<section class="sheet letterhead">
  <header class="letterhead__header">
    <div class="photo-bulbs" role="img" aria-label="Foto: Reihe leuchtender Glühbirnen vor dunklem Hintergrund"></div>
    <div class="brand"><span class="brand__name">TROLVANE</span><span class="brand__sub">Elektrotechnik</span></div>
    <ul class="contact-list">
      <li><svg><use href="#icon-pin"/></svg>Im Lindengrund 7 47391 Wendelstedt</li>
      <li><svg><use href="#icon-phone"/></svg>04128-6350712</li>
      <li><svg><use href="#icon-mail"/></svg>info@trolvane-elektrotechnik.de</li>
    </ul>
  </header>

  <p class="return-address">Im Lindengrund 7 | 47391 Wendelstedt</p>
  <span class="fold-mark" style="top:287px"></span>
  <span class="fold-mark" style="top:493px"></span>

  <div class="footer-rule"></div>
  <div class="service-icons" style="left:0;top:660px">
    <svg style="left:24px"><use href="#icon-bulb"/></svg>
    <svg style="left:97px"><use href="#icon-bolt"/></svg>
    <svg style="left:175px"><use href="#icon-house"/></svg>
    <svg style="left:253px"><use href="#icon-solar"/></svg>
  </div>
  <svg class="service-band" style="top:689px" width="504" height="24" viewBox="0 0 504 24">
    <polygon points="0,0 308,0 301,12 0,12" fill="var(--slate)"/>
    <polygon points="313,0 504,0 504,24 0,24 0,12 306,12" fill="var(--yellow)"/>
    <g stroke="#fff" stroke-width="2.4"><line x1="75" y1="0" x2="68" y2="12"/><line x1="151" y1="0" x2="144" y2="12"/><line x1="230" y1="0" x2="223" y2="12"/></g>
    <g text-anchor="middle"><text x="37" y="9">Beleuchtung</text><text x="110" y="9">Elektroinstalltion</text><text x="188" y="9">Smart Home</text><text x="266" y="9">Photovoltaik</text></g>
  </svg>
  <div class="bank-details" style="left:312px">Kreiskasse Wendorn<br>IBAN:DE71430982160004197356<br>BIC:WKRNDEF1WDN</div>
  <div class="bank-details" style="left:418px">Finanzamt Hobrachtal<br>USt.-ID: DE574036218<br>Steuer Nr.:3196450721</div>
  <div class="web" style="left:343px;top:693px"><svg><use href="#icon-globe"/></svg>www.trolvane-elektrotechnik.de</div>
</section>

<!-- Umschlag Rückseite -->
<section class="envelope envelope--flap">
  <svg class="envelope__flap" width="557" height="80" viewBox="0 0 557 80">
    <path d="M0 0H557L533 72Q530 79 520 79H38Q28 79 25 72Z" fill="var(--ink)"/>
  </svg>
  <div class="brand"><span class="brand__name">TROLVANE</span><span class="brand__sub">Elektrotechnik</span></div>
</section>

<!-- Umschlag Vorderseite -->
<section class="envelope envelope--window">
  <div class="sender-banner">
    <div class="photo-bulbs" role="img" aria-label="Foto: Reihe leuchtender Glühbirnen vor dunklem Hintergrund"></div>
    <div class="brand"><span class="brand__name">TROLVANE</span><span class="brand__sub">Elektrotechnik</span></div>
  </div>
  <div class="service-icons" style="left:0;top:225px">
    <svg style="left:76px"><use href="#icon-bulb"/></svg>
    <svg style="left:149px"><use href="#icon-bolt"/></svg>
    <svg style="left:227px"><use href="#icon-house"/></svg>
    <svg style="left:305px"><use href="#icon-solar"/></svg>
  </div>
  <svg class="service-band" style="top:255px" width="557" height="24" viewBox="0 0 557 24">
    <polygon points="0,0 363,0 356,11 0,11" fill="var(--slate)"/>
    <polygon points="368,0 557,0 557,24 0,24 0,11 361,11" fill="var(--yellow)"/>
    <g stroke="#fff" stroke-width="2.4"><line x1="127" y1="0" x2="120" y2="11"/><line x1="204" y1="0" x2="197" y2="11"/><line x1="283" y1="0" x2="276" y2="11"/></g>
    <g text-anchor="middle"><text x="89" y="8.5">Beleuchtung</text><text x="162" y="8.5">Elektroinstalltion</text><text x="240" y="8.5">Smart Home</text><text x="318" y="8.5">Photovoltaik</text></g>
  </svg>
  <div class="sender-address"><svg><use href="#icon-pin"/></svg>Im Lindengrund 7 · 47391 Wendelstedt</div>
  <div class="web" style="left:391px;top:257px"><svg><use href="#icon-globe"/></svg>www.trolvane-elektrotechnik.de</div>
</section>

</body>
</html>
```